Facebook Banner

Hi, I need help making banners for my social media channels. Once we make one banner all the other banners will follow the same look and feel. Please help me design my Facebook page banner to start.

Attached is my branding guidelines - please choose a design that fits within my Branding Guidelines. Please note that I only use two fonts. Belanosima and Arial. I have also attached screenshots of my Youtube channel and Tiktok thumbnails. I made banners already but I am not happy with them. Please take into account my whole “brand universe” to create the banner.

The message I want to convey in the banner is that I offer tours of factories in Vietnam. I offer to take clients on factory tours and the tours include car, driver and translator.

If you have any questions then please don't hesitate to ask.

I have included images of factory tours. I also included my logo in case you want to use it.

```html
<!DOCTYPE html>
<html lang="en">
<head>
<meta charset="utf-8">
<title>Shoe Factory Tour Banner</title>
<link rel="stylesheet" href="https://fonts.googleapis.com/css2?family=Belanosima:wght@400;700&family=Arimo:wght@400;700&display=swap">
<style>
  :root {
    --plum-deep: #240c33;
    --magenta: #b3237a;
    --magenta-bright: #d0348f;
    --headline-white: #ffffff;
    --headline-yellow: #f4f06a;
    --headline-pink: #d6338f;
    --body-text: #f3ecf5;
    --cta-pink: #ff9fd3;
    --button-fill: #fbf6c8;
    --button-text: #561048;
    --rule: rgba(214, 51, 143, 0.55);
  }
  * { margin: 0; padding: 0; box-sizing: border-box; }
  html, body { width: 1200px; height: 1200px; overflow: hidden; background: var(--plum-deep); }
  .banner {
    position: relative;
    width: 1200px;
    height: 1200px;
    overflow: hidden;
    font-family: Arimo, Arial, sans-serif;
  }
  .factory-photo {
    position: absolute;
    top: 0; right: 0;
    width: 560px; height: 1200px;
    background: linear-gradient(180deg, #c9c3bd 0%, #9fb6c4 25%, #6e7d8c 55%, #3b3b40 75%, #d9d6d2 100%);
  }
  .panel-shapes {
    position: absolute;
    inset: 0;
    width: 1200px; height: 1200px;
  }
  .brand-name {
    position: absolute;
    left: 52px; top: 78px;
    display: flex; align-items: center; gap: 14px;
    font-family: Belanosima, Arial, sans-serif;
    font-weight: 700;
    font-size: 36px;
    color: var(--headline-white);
    line-height: 1;
  }
  .brand-mark {
    width: 32px; height: 32px;
    background: var(--magenta-bright);
  }
  .headline {
    position: absolute;
    left: 50px; top: 206px;
    font-family: Belanosima, Arial, sans-serif;
    font-weight: 700;
    font-size: 78px;
    line-height: 1.14;
    text-transform: uppercase;
    letter-spacing: 1px;
  }
  .headline span { display: block; }
  .headline .line-white { color: var(--headline-white); }
  .headline .line-yellow { color: var(--headline-yellow); }
  .headline .line-pink { color: var(--headline-pink); }
  .divider {
    position: absolute;
    left: 30px;
    width: 560px; height: 2px;
    background: linear-gradient(90deg, transparent, var(--rule) 20%, var(--rule) 80%, transparent);
  }
  .divider-top { top: 494px; }
  .divider-bottom { top: 811px; }
  .intro {
    position: absolute;
    left: 57px; top: 528px;
    width: 500px;
    color: var(--body-text);
    font-size: 18px;
    line-height: 1.34;
  }
  .intro p + p { margin-top: 24px; margin-left: -4px; }
  .tour-photo {
    position: absolute;
    left: 430px; top: 745px;
    width: 388px; height: 388px;
    border-radius: 50%;
    border: 11px solid var(--magenta);
    background: radial-gradient(circle at 50% 35%, #dfe4ea 0%, #b9b3ab 45%, #6b5a4c 80%, #4a3b33 100%);
  }
  .cta-question {
    position: absolute;
    left: 58px; top: 990px;
    width: 330px;
    color: var(--cta-pink);
    font-weight: 700;
    font-size: 19px;
    line-height: 1.35;
  }
  .cta-button {
    position: absolute;
    left: 42px; top: 1060px;
    width: 385px; height: 86px;
    border-radius: 14px;
    background: var(--button-fill);
    color: var(--button-text);
    font-family: Belanosima, Arial, sans-serif;
    font-weight: 700;
    font-size: 29px;
    line-height: 1.02;
    text-transform: uppercase;
    text-align: center;
    display: flex; align-items: center; justify-content: center;
  }
</style>
</head>
<body>
<main class="banner">
  <div class="factory-photo" role="img" aria-label="Photo of visitors inspecting racks of finished leather shoes inside a shoe factory workshop"></div>

  <svg class="panel-shapes" viewBox="0 0 1200 1200" aria-hidden="true">
    <defs>
      <linearGradient id="panelFill" x1="0" y1="0" x2="0" y2="1">
        <stop offset="0" stop-color="#220b30"/>
        <stop offset="0.55" stop-color="#2e0f3c"/>
        <stop offset="1" stop-color="#3c1248"/>
      </linearGradient>
      <linearGradient id="lowerWave" x1="0" y1="0" x2="1" y2="1">
        <stop offset="0" stop-color="#6a155a"/>
        <stop offset="1" stop-color="#b0237a"/>
      </linearGradient>
    </defs>
    <path d="M0,0 H740 C790,260 830,520 812,780 C800,940 760,1080 720,1200 H0 Z" fill="var(--magenta)"/>
    <path d="M0,0 H712 C760,260 800,520 782,780 C770,940 730,1080 692,1200 H0 Z" fill="url(#panelFill)"/>
    <path d="M0,870 C180,840 380,880 560,850 C660,835 730,810 790,790 C780,950 740,1080 700,1200 H0 Z" fill="url(#lowerWave)"/>
  </svg>

  <div class="brand-name"><span class="brand-mark"></span>Lotus Site Visits</div>

  <h1 class="headline">
    <span class="line-white">Visiting Shoe</span>
    <span class="line-yellow">Factory In</span>
    <span class="line-pink">Vietnam</span>
  </h1>

  <div class="divider divider-top"></div>

  <div class="intro">
    <p>We take you inside real factories across Vietnam, so you can meet manufacturers face to face and check quality on the spot.</p>
    <p>Every tour includes a private car, a professional driver and a translator, so you can focus on finding the right partner for your products while we handle the travel and the talking.</p>
  </div>

  <div class="divider divider-bottom"></div>

  <div class="tour-photo" role="img" aria-label="Round photo of a small group of visitors looking at shoe racks in a factory room"></div>

  <p class="cta-question">Want to find a manufacturer in Vietnam for your products?</p>
  <div class="cta-button">Contact us to book<br>a factory tour!</div>
</main>
</body>
</html>
```